Project, Programme and Portfolio Management Consultant needs a business card

I have recently had someone create a brand guide for me and I wish to have new business cards that incorporate the new brand. I am an independent management consultant working with businesses to improve their ability to deliver their business strategy through selecting the right project, the right people and doing it in the right way. Whilst I am currently working on my own, I am hoping to start to build win business where I need to bring in a team and this branding activity is the start of that process.

Target Market(s)

Medium to large businesses, government departments and defence

Contact Information for Business Card

Name
job title
business name
mobile
email
website
linkedIn profile

Font styles to use
Other font styles liked:
• roboto light

Colors

Designer to choose colors to be used in the design.

Requirements
Must have
• Must use my logo and brand colours (see attached brand guide)

```html
<!DOCTYPE html>
<html lang="en">
<head>
<meta charset="utf-8">
<title>Trivane Advisory — Business Card</title>
<link href="https://fonts.googleapis.com/css2?family=Lato:wght@400;700;900&display=swap" rel="stylesheet">
<style>
  :root {
    --stage: #2a2a2c;
    --card: #1a1f33;
    --gold: #e5ad26;
    --teal: #1fa79c;
    --shadow: rgba(0,0,0,0.45);
  }
  * { margin: 0; padding: 0; box-sizing: border-box; }
  html, body {
    width: 1200px; height: 970px; overflow: hidden;
    background: var(--stage);
    font-family: "Lato", Arial, sans-serif;
  }
  .card {
    position: absolute;
    width: 560px; height: 320px;
    background: var(--card);
    border-bottom: 4px solid var(--gold);
    box-shadow: 0 10px 24px var(--shadow);
  }
  .card--front { left: 80px; top: 90px; }
  .card--back { left: 560px; top: 560px; }

  .identity { position: absolute; left: 0; top: 48px; }
  .identity__bar {
    position: absolute; left: 18px; top: 6px;
    width: 14px; height: 34px; background: var(--gold);
  }
  .identity__name {
    position: absolute; left: 46px; top: 0;
    font-weight: 900; font-size: 26px; color: var(--gold); white-space: nowrap;
  }
  .identity__title {
    position: absolute; left: 48px; top: 32px;
    font-size: 13px; color: var(--teal); white-space: nowrap; letter-spacing: 0.3px;
  }

  .details { position: absolute; left: 48px; top: 150px; font-size: 13px; line-height: 17px; }
  .details__company { color: var(--gold); letter-spacing: 0.4px; }
  .details__address { color: var(--teal); }
  .contacts { list-style: none; margin-top: 10px; }
  .contacts li {
    display: flex; align-items: center; gap: 10px;
    color: var(--teal); height: 20px;
  }
  .contacts svg { width: 14px; height: 14px; flex: none; }

  .brand {
    position: absolute;
    font-weight: 700; color: var(--gold);
    letter-spacing: 5px; white-space: nowrap;
  }
  .card--front .brand { right: 48px; top: 190px; font-size: 30px; }
  .card--back .brand { left: 50%; top: 50%; transform: translate(-50%, -50%); font-size: 38px; }
</style>
</head>
<body>

<section class="card card--front" aria-label="Business card front">
  <div class="identity">
    <span class="identity__bar"></span>
    <h1 class="identity__name">Avery Holt</h1>
    <p class="identity__title">Founder &amp; CEO</p>
  </div>

  <div class="details">
    <p class="details__company">TRIVANE ADVISORY LLC</p>
    <p class="details__address">48 Harbor Lane,<br>2nd FL Portland, ME 04101</p>
    <ul class="contacts">
      <li>
        <svg viewBox="0 0 16 16" aria-hidden="true"><path fill="#e5ad26" d="M3.6 1.5l2.3 2.4-1.3 1.8c.9 2 2.6 3.7 4.6 4.6l1.8-1.3 2.4 2.3-1.2 2.2C7 14.8 1.2 9 1.5 2.7z"/></svg>
        5550147823
      </li>
      <li>
        <svg viewBox="0 0 16 16" aria-hidden="true"><rect x="1" y="3" width="14" height="10" fill="#e5ad26"/><path d="M1.5 3.5L8 9l6.5-5.5" fill="none" stroke="#1a1f33" stroke-width="1.3"/></svg>
        hello@trivane.co
      </li>
      <li>
        <svg viewBox="0 0 16 16" aria-hidden="true"><g fill="none" stroke="#e5ad26" stroke-width="1.2"><circle cx="8" cy="8" r="6.5"/><ellipse cx="8" cy="8" rx="2.8" ry="6.5"/><path d="M1.5 8h13M2.5 5h11M2.5 11h11"/></g></svg>
        www.trivane.co
      </li>
      <li>
        <svg viewBox="0 0 16 16" aria-hidden="true"><circle cx="8" cy="8" r="6.5" fill="none" stroke="#e5ad26" stroke-width="1.2"/></svg>
        network.example/averyholt
      </li>
    </ul>
  </div>

  <p class="brand">TRIVANE</p>
</section>

<section class="card card--back" aria-label="Business card back">
  <p class="brand">TRIVANE</p>
</section>

</body>
</html>
```